Flyer Design - High Quality

*** Although this current job contest is listed as a ‘one-off contest’ we are also looking at working with a graphic designer long-term, which will include quite regular design work. So even though this is just a small job, if you want to & you do a good job on this, we would love to look at working with you on a regular basis.
* The winning designer will also get a freelance job designing another flyer in same design
Job Basics:
1. the design of a ….
Promotional corporate flyer - size = A4 - approx 6 or 7 pages.
*** The design will need to be extremely high quality/professional. Must be of a similar or better standard as the attached flyers – 1) Ross Penley_Info Pack & 2) DrGlen Whitcombe
* Please view these flyers first to ensure you can create a flyer of similar or better quality before proceeding.
Specific Requirements:
1. high-quality, professional promotional flyer [size = A4 - for online use predominantly . I.e. not for printing necessarily] using the text, images and basic instructions outlined on the word document attached - 'Flyer_All talks in 1_guidelines'.
2. Examples of similar quality (good) designs = 1) Ross Penley_Info Pack & 2) DrGlen Whitcombe
Background:
I am a motivational speaker on health, well-being and work-life balance. This flyer is to be used for promotional purposes when clients inquire about me speaking at their conference. Ross Penley & Glen Whitcombe are speakers who do somewhat similar talks to me, and who have flyers that I really like.
Theme: My general theme is ‘health and well-being’ (we're a little bit more towards natural health and Eastern medicine, but don't want it too ‘eastern’ if you know what I mean).
Main Look & Feel … to be conveyed:
Professional / Corporate
Health, Vitality and happiness (fresh, modern and vital)
eye-catching / attention grabbing
* The design should represent a balance between highly sophisticated, professional and classy - corporate savvy - with a hint of 'natural health, Eastern wisdom and a general ‘high energy/fresh health and vitality feel'. While we would like the design to convey some aspect of ‘ natural/Eastern’ wisdom), we predominantly want to convey the idea of ‘modern’ health (i.e. fresh, modern and vital).
Colours:
We are open to your creative suggestions, but were generally thinking something along the lines of the colours in our corporate logo –
dark blue, aqua blue, grey – see logo (KVT_300kb.jpg) in attachments
- possibly with some bright green, orange etc if you think it might suit – to help give it the ‘natural health’ feel.
* Notes:
1. SAVING YOUR TIME: If you just want to start just doing a quickish design of the first 1-2 pages and submitting that (images for these pages attached - though use own images if you think they are better), then that’s fine. Then we can let you know if it is along the lines of something we like or not. This way, you can do something relatively quickly, without wasting too much time, if it is definitely not something we like. Hope that helps - we are always conscious of trying to make things good for you as a designer too.
2. Do not feel completely bound to the ideas suggested/asked for. Feel free to convey the basic ideas/keys but feel free to use/follow some of your own ideas/creative desires.
3. Any photos/images should be royalty free (or ask us if we want to pay for it) and not widely used or seen in the public domain - i.e. we don’t want people to have seen the photo/image elsewhere (within reason).
Thanks a lot and look forward to receiving your first design!
Cheers
Owen
Target Market(s)
Predominantly corporates / business groups.
Industry/Entity Type
Graphic Designer

```html
<!DOCTYPE html>
<html lang="en">
<head>
<meta charset="utf-8">
<title>Achieving A Work Life High</title>
<link href="https://fonts.googleapis.com/css2?family=Gochi+Hand&family=Open+Sans:ital,wght@0,400;0,600;0,700;1,400;1,700&display=swap" rel="stylesheet">
<style>
  :root {
    --page-bg: #ffffff;
    --sheet-light: #e6f3fa;
    --sheet-mid: #c4e0ee;
    --navy: #0d4f8b;
    --title-blue: #1b5c9c;
    --panel-grey: #5f6e78;
    --text-dark: #222a30;
    --white: #ffffff;
    --photo-deep: #3f7fc4;
    --photo-light: #b9d6ee;
  }
  * { box-sizing: border-box; margin: 0; padding: 0; }
  html, body { width: 1200px; height: 900px; overflow: hidden; background: var(--page-bg); }
  body { position: relative; font-family: "Open Sans", Arial, sans-serif; color: var(--text-dark); }

  .sheet {
    position: absolute; left: 27px; top: 42px; width: 1146px; height: 813px;
    background: linear-gradient(135deg, var(--sheet-light) 0%, var(--sheet-mid) 100%);
  }
  .side-band {
    position: absolute; left: 27px; top: 93px; width: 87px; height: 711px;
    background: var(--navy); border-radius: 0 9px 9px 0;
  }
  .feature-panel {
    position: absolute; left: 714px; top: 93px; width: 459px; height: 693px;
    background: var(--panel-grey); border-radius: 12px 0 0 12px; overflow: hidden;
  }
  .feature-panel .values {
    position: absolute; left: 19px; top: 222px;
    color: var(--white); font-weight: 700; font-size: 27px; line-height: 36px;
  }
  .feature-panel .photo {
    position: absolute; left: 19px; top: 384px; right: 0; bottom: 0;
    border-radius: 10px 0 0 10px;
    background: linear-gradient(to bottom, var(--photo-deep), var(--photo-light));
  }

  .title {
    position: absolute; left: 148px; top: 80px;
    font-family: "Gochi Hand", cursive; color: var(--title-blue); font-weight: 400;
  }
  .title .line1 { display: block; font-size: 68px; line-height: 64px; }
  .title .line2 { display: block; font-size: 90px; line-height: 80px; }

  .intro {
    position: absolute; left: 150px; top: 264px; width: 492px;
    font-size: 12.3px; line-height: 19.5px;
  }
  .intro p { margin-bottom: 19.5px; }
  .intro p.joined { margin-bottom: 0; }

  .choice-heading {
    position: absolute; left: 150px; top: 468px;
    font-size: 13.2px; font-weight: 700; letter-spacing: 0.2px;
  }
  .benefits {
    position: absolute; left: 150px; top: 498px; width: 440px; list-style: none;
    font-size: 12.3px; line-height: 18px;
  }
  .benefits li { position: relative; padding-left: 22px; margin-bottom: 8px; }
  .benefits svg { position: absolute; left: 0; top: 2px; width: 14px; height: 14px; }

  .testimonial { position: absolute; left: 150px; top: 750px; font-size: 12.3px; line-height: 19px; }
  .testimonial .quote { font-weight: 700; font-style: italic; }
  .testimonial .source { font-style: italic; }
</style>
</head>
<body>
  <div class="sheet" role="img" aria-label="Soft light-blue decorative swirl pattern background"></div>
  <div class="side-band"></div>

  <h1 class="title"><span class="line1">Achieving A</span><span class="line2">Work Life High</span></h1>

  <div class="intro">
    <p>Does your group have demanding jobs, work long hours, find it tough balancing their personal and professional lives or simply want to de-stress,<br>re-energise, and be re-motivated?</p>
    <p class="joined">Would you like your group to learn some simple, user-friendly tips for achieving better health, greater motivation, productivity and performance, as well as a happier work-life balance … all while having a bit of fun?</p>
    <p>If so, whether for an inspiring keynote, some in-house training, or a entertaining conference breakout/workshop, one of Owen Harlow’s ‘Work-Life High’ sessions may be just what you’re after.</p>
  </div>

  <h2 class="choice-heading">OWEN IS A GREAT CHOICE IF YOU WANT…</h2>
  <ul class="benefits">
    <li><svg viewBox="0 0 14 14"><circle cx="7" cy="7" r="7" fill="var(--navy)"/><path d="M5.5 4 L8.5 7 L5.5 10" stroke="#fff" stroke-width="1.8" fill="none"/></svg>an industry leader who is highly entertaining, yet highly practical<br>&amp; down to earth</li>
    <li><svg viewBox="0 0 14 14"><circle cx="7" cy="7" r="7" fill="var(--navy)"/><path d="M5.5 4 L8.5 7 L5.5 10" stroke="#fff" stroke-width="1.8" fill="none"/></svg>something different to the usual (boring) health &amp; performance info - ‘Eastern wisdoms’</li>
    <li><svg viewBox="0 0 14 14"><circle cx="7" cy="7" r="7" fill="var(--navy)"/><path d="M5.5 4 L8.5 7 L5.5 10" stroke="#fff" stroke-width="1.8" fill="none"/></svg>the secrets of the world’s healthiest individuals &amp; highest performing businesspeople</li>
    <li><svg viewBox="0 0 14 14"><circle cx="7" cy="7" r="7" fill="var(--navy)"/><path d="M5.5 4 L8.5 7 L5.5 10" stroke="#fff" stroke-width="1.8" fill="none"/></svg>simple strategies to increase energy &amp; reduce stress … by up to 50%</li>
    <li><svg viewBox="0 0 14 14"><circle cx="7" cy="7" r="7" fill="var(--navy)"/><path d="M5.5 4 L8.5 7 L5.5 10" stroke="#fff" stroke-width="1.8" fill="none"/></svg>to take attendees productivity, motivation and results to new levels</li>
    <li><svg viewBox="0 0 14 14"><circle cx="7" cy="7" r="7" fill="var(--navy)"/><path d="M5.5 4 L8.5 7 L5.5 10" stroke="#fff" stroke-width="1.8" fill="none"/></svg>real tips for ‘making things practical’ in hectic, high-stress, high-pressure roles</li>
    <li><svg viewBox="0 0 14 14"><circle cx="7" cy="7" r="7" fill="var(--navy)"/><path d="M5.5 4 L8.5 7 L5.5 10" stroke="#fff" stroke-width="1.8" fill="none"/></svg>a good laugh and a bit of fun</li>
  </ul>

  <div class="testimonial">
    <p class="quote">“Brilliant…Rating = 100%”</p>
    <p class="source">Jenna Morrow – Office of Workforce Programs</p>
  </div>

  <div class="feature-panel">
    <p class="values">High Energy,<br>Low Stress,<br>Life Balance,<br>Work Success</p>
    <div class="photo" role="img" aria-label="Photo of two business people jumping for joy under a bright open sky"></div>
  </div>
</body>
</html>
```